Website Design: Neuroscience research lab at an academic University.

I am looking to redo my University website for Neuroscience Research. <br/><br/>I am looking for a clean, modern and organized design to publish our work. Although I want a modern look, the focus should be on the text content.<br/><br/>Pages I need. These pages should be in the navigation bar;<br/>*Home*: with overview of the lab, contact information, and possibly with <br/>"Recent News and Events" information<br/>*Research*/Projects: will have text description, images, as well as video of various research projects we have done or are working on<br/>*People*: Personnel page with photos and bios of the team<br/>*Publications*: List of research articles with hyperlinks to online <br/>versions of articles as well as PDFs<br/>*News*: Continually updated list of events<br/><br/><br/>Some designs I like: <br/><br/>https://www.moravinlabs.example/<br/>http://www.quillbranch.example/<br/>https://tovernilab.example<br/>http://www.gradmerlab.example/<br/>https://vkot.halvern.example/

Target Market(s)

Academics, university students, government

Logo Text

Morvek Lab

Number of Pages Required

5+ page

Colors

Designer to choose colors to be used in the design.

Requirements
Must have
• A modern but elegant design that focuses on the research but that is also visually appealing.
• For the logo, please see the sketch in the attached files. That is a rough sketch of a logo that you can base your logo design on.
Should not have
• No search bar

```html
<!DOCTYPE html>
<html lang="en">
<head>
<meta charset="utf-8">
<title>Morvek Lab — Neuroscience Research Lab</title>
<link rel="stylesheet" href="https://fonts.googleapis.com/css2?family=Montserrat:wght@300;400;500;600&display=swap">
<style>
:root{
  --blue:#2f8ae0;
  --blue-dark:#1f6fc0;
  --ink:#2b2b2b;
  --muted:#6d6d6d;
  --faint:#9a9a9a;
  --rule:#e3e3e3;
  --band:#f6f6f6;
  --white:#ffffff;
}
*{box-sizing:border-box;margin:0;padding:0}
html,body{width:1200px;height:3599px;overflow:hidden}
body{font-family:'Montserrat',sans-serif;color:var(--ink);background:var(--white);position:relative}
.abs{position:absolute}
a{color:inherit;text-decoration:none}

/* hero */
.hero{position:absolute;left:0;top:0;width:1200px;height:600px;
  background:
    radial-gradient(ellipse 420px 300px at 130px 520px,#d2452a 0%,rgba(210,69,42,0) 70%),
    radial-gradient(ellipse 500px 320px at 980px 230px,#c65a2a 0%,rgba(198,90,42,0) 70%),
    radial-gradient(ellipse 360px 260px at 560px 90px,#2a3fb0 0%,rgba(42,63,176,0) 70%),
    radial-gradient(ellipse 300px 200px at 1120px 80px,#3e8f5a 0%,rgba(62,143,90,0) 70%),
    linear-gradient(135deg,#1b2a3a 0%,#26213a 45%,#3b2323 100%)}
.brand{position:absolute;display:flex;align-items:center;gap:14px}
.brand-mark{width:58px;height:58px;border-radius:50%;background:#6aa8e8}
.brand-name{font-weight:300;font-size:21px;letter-spacing:1px;text-transform:uppercase}
.hero .brand{left:120px;top:26px;color:var(--white)}
.nav{position:absolute;top:53px;left:495px;display:flex;gap:27px;font-size:12px;color:var(--white);font-weight:500}
.nav .active{color:var(--blue)}
.nav-underline{position:absolute;left:488px;top:118px;width:52px;height:2px;background:var(--blue)}
.nav-rule{position:absolute;left:40px;top:119px;width:1120px;height:1px;background:rgba(255,255,255,.25)}
.btn-pub{position:absolute;left:960px;top:43px;width:120px;height:32px;border:1px solid var(--white);color:var(--white);font-size:12px;display:flex;align-items:center;justify-content:center;font-weight:500}
.hero-title{position:absolute;top:268px;width:1200px;text-align:center;color:var(--white);font-weight:300;font-size:48px}
.hero-sub{position:absolute;top:328px;width:1200px;text-align:center;color:var(--white);font-weight:300;font-size:28px}
.hero-cta{position:absolute;top:506px;width:1200px;text-align:center;color:var(--white);font-size:14px;font-weight:500}
.hero-arrow{position:absolute;left:591px;top:545px}
.hero-dots{position:absolute;left:1133px;top:322px;display:flex;flex-direction:column;gap:5px}
.hero-dots span{width:8px;height:8px;border:1px solid #fff;border-radius:50%}

/* section heading */
.sec-title{position:absolute;width:1200px;text-align:center;font-weight:300;font-size:29px;color:var(--ink)}
.sec-title::after{content:"";display:block;width:40px;height:1px;background:var(--faint);margin:10px auto 0}

/* research cards */
.card{position:absolute;top:720px;width:240px}
.card-media{width:240px;height:160px}
.card h3{margin-top:20px;font-size:15px;font-weight:500;line-height:20px}
.card.featured h3{color:var(--blue)}
.card p{margin-top:18px;font-size:11.5px;line-height:19.5px;color:var(--muted)}
.btn{display:flex;align-items:center;justify-content:center;width:120px;height:32px;border:1px solid var(--blue);color:var(--blue);font-size:11.5px;font-weight:500}
.btn.solid{background:var(--blue);color:var(--white)}
.card .btn{position:absolute;top:340px}

/* feature band */
.feature{position:absolute;left:0;top:1148px;width:1200px;height:480px;background:linear-gradient(180deg,#f3f3f3,#fafafa)}
.feature-art{position:absolute;left:165px;top:48px;width:405px;height:390px;border-radius:48% 52% 40% 60%/50% 45% 55% 50%;background:radial-gradient(circle at 45% 40%,#7db8f0,#3f8ee0)}
.feature-copy{position:absolute;left:620px;top:88px;width:460px}
.eyebrow{font-size:11px;font-weight:600;color:var(--blue)}
.feature-copy h2{margin-top:14px;font-weight:300;font-size:30px;line-height:37px}
.feature-copy p{margin-top:24px;font-size:11.5px;line-height:19.5px;color:var(--muted);text-align:justify}
.feature-copy .btn{margin-top:40px}

/* news */
.event{position:absolute;left:120px;top:1748px;width:460px;height:459px;background:#3a3a3a}
.event-media{position:absolute;left:0;top:0;width:460px;height:459px;background:linear-gradient(135deg,#aeb7b3 0%,#6f7672 45%,#2f2f30 100%)}
.event-tag{position:absolute;left:18px;top:22px;color:var(--white);font-size:11px;font-weight:600}
.event-dots{position:absolute;right:20px;top:26px;display:flex;gap:7px}
.event-dots span{width:8px;height:8px;border:1px solid #fff;border-radius:50%}
.event-box{position:absolute;left:0;top:300px;width:360px;height:159px;background:var(--white);padding:36px 20px 0}
.event-date{font-size:10px;color:var(--faint);display:flex;align-items:center;gap:6px}
.event-box h4{margin-top:8px;font-size:14.5px;font-weight:500;line-height:20px}
.event-box .more{display:block;margin-top:20px;font-size:11.5px;color:var(--blue);font-weight:500}
.news{position:absolute;left:620px;top:1770px;width:460px}
.news-item{display:flex;gap:15px;padding:22px 0;border-bottom:1px solid var(--rule)}
.news-item:first-of-type{margin-top:25px}
.avatar{width:68px;height:68px;border-radius:50%;flex:none}
.news-item p{font-size:11.3px;line-height:18px;margin-top:4px}
.news-item.current p{color:var(--blue)}
.news-item time{display:block;margin-top:8px;font-size:9.5px;color:var(--muted);letter-spacing:.5px}
.view-all{display:block;margin-top:32px;font-size:11.5px;color:var(--blue);font-weight:500}

.neuron-band{position:absolute;left:0;top:2263px;width:1200px;height:320px;background:radial-gradient(ellipse 500px 200px at 850px 140px,#9fb3bd 0%,rgba(159,179,189,0) 70%),linear-gradient(180deg,#557380,#6e8d98 60%,#8aa4ad)}

/* people */
.person{position:absolute;top:2712px;width:240px;text-align:center}
.portrait{width:210px;height:200px;margin:0 auto;border-radius:46% 54% 42% 58%/50% 48% 52% 50%}
.person h5{margin-top:16px;font-size:19px;font-weight:500}
.person.featured h5{color:var(--blue)}
.person span{display:block;margin-top:4px;font-size:11.5px;color:var(--muted)}
.people-dots{position:absolute;top:3015px;left:563px;display:flex;gap:7px}
.people-dots span{width:9px;height:9px;border:1px solid var(--blue);border-radius:50%}
.people-dots span:first-child{background:radial-gradient(circle,var(--blue) 35%,transparent 40%)}

/* publications */
.pubs{position:absolute;left:0;top:3080px;width:1200px;height:159px;background:var(--blue);color:var(--white)}
.pubs h2{position:absolute;left:118px;top:50px;font-weight:300;font-size:29px}
.pubs p{position:absolute;left:118px;top:92px;font-size:14px;font-weight:300}
.pubs .btn{position:absolute;left:840px;top:58px;width:240px;height:40px;border-color:var(--white);color:var(--white);font-size:11.5px}

/* footer */
.footer .brand{left:120px;top:3305px;color:#5a5a5a}
.quick{position:absolute;left:620px;top:3316px;font-size:11.5px;color:#5a5a5a;line-height:29px}
.quick b{color:var(--blue);font-weight:600}
.contact{position:absolute;right:121px;top:3315px;text-align:right}
.contact .call{font-size:28px;font-weight:300}
.contact .mail{font-size:15px;font-weight:500;margin-top:4px;color:#4a4a4a}
.contact .hours{font-size:8.5px;color:var(--faint);letter-spacing:1px;margin-top:12px}
.social{position:absolute;top:3414px;left:921px;display:flex;gap:10px}
.social span{width:32px;height:32px;border-radius:50%}
.foot-rule{position:absolute;left:40px;top:3545px;width:1120px;height:1px;background:var(--rule)}
.copyright{position:absolute;left:120px;top:3566px;font-size:9.5px;color:var(--muted)}
</style>
</head>
<body>

<header class="hero" role="img" aria-label="Colourful fluorescent microscopy image of brain tissue in blue, orange and red">
  <div class="brand"><span class="brand-mark"></span><span class="brand-name">Morvek Lab</span></div>
  <nav class="nav">
    <a class="active">Home</a><a>About</a><a>Research</a><a>People</a><a>News / Event</a><a>Contact</a>
  </nav>
  <div class="nav-rule"></div>
  <div class="nav-underline"></div>
  <a class="btn-pub">Publications</a>
  <h1 class="hero-title">Neuroscience Research Lab</h1>
  <p class="hero-sub">A search for a neural syntax</p>
  <p class="hero-cta">Our Research</p>
  <svg class="hero-arrow" width="18" height="24" viewBox="0 0 18 24" fill="none" stroke="#fff" stroke-width="1.5"><path d="M9 2v19M2 14l7 7 7-7"/></svg>
  <div class="hero-dots"><span></span><span></span><span></span><span></span><span></span><span></span></div>
</header>

<h2 class="sec-title" style="top:640px">A Search for a Neural Syntax</h2>

<article class="card featured" style="left:60px">
  <div class="card-media" role="img" aria-label="Research video: EEG cap on a subject" style="background:linear-gradient(135deg,#7fb5b0,#5f9b98)"></div>
  <h3>Lorem ipsum dolor sit amet, consectetur adipiscing</h3>
  <p>Sed do eiusmod tempor incididunt ut labore et dolore magna aliqua. Ut enim ad minim veniam, quis nostrud exercitation ullamco ...</p>
  <a class="btn solid">Learn More</a>
</article>
<article class="card" style="left:340px">
  <div class="card-media" role="img" aria-label="Black and white neuron network" style="background:linear-gradient(135deg,#d8d8d8,#6b6b6b)"></div>
  <h3>Lorem ipsum dolor sit amet, consectetur adipiscing</h3>
  <p>Sed do eiusmod tempor incididunt ut labore et dolore magna aliqua. Ut enim ad minim veniam, quis nostrud exercitation ullamco ...</p>
  <a class="btn">Learn More</a>
</article>
<article class="card" style="left:620px">
  <div class="card-media" role="img" aria-label="Research video: blue and yellow neurons" style="background:linear-gradient(135deg,#e4b23a,#3d7ac8 60%,#2b5fa8)"></div>
  <h3>Lorem ipsum dolor sit amet, consectetur adipiscing</h3>
  <p>Sed do eiusmod tempor incididunt ut labore et dolore magna aliqua. Ut enim ad minim veniam, quis nostrud exercitation ullamco ...</p>
  <a class="btn">Learn More</a>
</article>
<article class="card" style="left:900px">
  <div class="card-media" role="img" aria-label="Purple and cyan stained tissue" style="background:linear-gradient(135deg,#a63fd0,#2a1b4a 55%,#3fb7d8)"></div>
  <h3>Lorem ipsum dolor sit amet, consectetur adipiscing</h3>
  <p>Sed do eiusmod tempor incididunt ut labore et dolore magna aliqua. Ut enim ad minim veniam, quis nostrud exercitation ullamco ...</p>
  <a class="btn">Learn More</a>
</article>

<section class="feature">
  <div class="feature-art" role="img" aria-label="Low-poly blue brain illustration"></div>
  <div class="feature-copy">
    <p class="eyebrow">Simply dummy text of the web</p>
    <h2>Ut enim ad minim veniam,<br>qu tis nostrud ullamco</h2>
    <p>Lorem ipsum dolor sit amet, consectetur adipiscing elit, sed do eiusmod tempor incididunt ut labore et dolore magna aliqua. Ut enim ad minim veniam, quis nostrud exercitation ullamco laboris nisi ut aliquip ex ea commodo consequat. Duis aute irure dolor in reprehenderit in voluptate velit esse cillum dolore eu fugiat nulla pariatur. Excepteur sint occaecat cupidatat non proident, sunt in culpa qui officia deserunt mollit anim id est laborum.</p>
    <a class="btn">Learn More</a>
  </div>
</section>

<h2 class="sec-title" style="top:1672px">What’s New?</h2>

<article class="event">
  <div class="event-media" role="img" aria-label="Researcher working at a desk"></div>
  <span class="event-tag">Upcoming Event</span>
  <div class="event-dots"><span></span><span></span><span></span></div>
  <div class="event-box">
    <p class="event-date"><svg width="11" height="11" viewBox="0 0 11 11" fill="none" stroke="#9a9a9a"><rect x=".5" y="1.5" width="10" height="9"/><path d="M.5 4h10"/></svg>MAY 7, 2019 @ 2:00</p>
    <h4>Excepteur sint occaecat cupidatat non proident, sunt in culpa qui</h4>
    <a class="more">More Info</a>
  </div>
</article>

<section class="news">
  <p class="eyebrow">Latest News</p>
  <div class="news-item current">
    <div class="avatar" role="img" aria-label="News thumbnail photo" style="background:#8a8f92"></div>
    <div><p>It is a long established fact that a reader will be distracted by the readable content of a page when looking ...</p><time>MAY 7, 2019</time></div>
  </div>
  <div class="news-item">
    <div class="avatar" role="img" aria-label="Neuron thumbnail" style="background:#b5b5b5"></div>
    <div><p>It is a long established fact that a reader will be distracted by the readable content of a page when looking ...</p><time>MAY 7, 2019</time></div>
  </div>
  <div class="news-item">
    <div class="avatar" role="img" aria-label="Neural network thumbnail" style="background:#5c5c5c"></div>
    <div><p>It is a long established fact that a reader will be distracted by the readable content of a page when looking ...</p><time>MAY 7, 2019</time></div>
  </div>
  <a class="view-all">View All News</a>
</section>

<div class="neuron-band" role="img" aria-label="Glassy teal neuron close-up"></div>

<h2 class="sec-title" style="top:2627px">Our People</h2>

<div class="person featured" style="left:60px">
  <div class="portrait" role="img" aria-label="Portrait of Teodor Vanhalt" style="background:linear-gradient(135deg,#c9a778,#6d5846)"></div>
  <h5>Teodor Vanhalt</h5><span>Halden Professor of Neuroscience</span>
</div>
<div class="person" style="left:340px">
  <div class="portrait" role="img" aria-label="Portrait of Ilse Marquand" style="background:linear-gradient(135deg,#8b6a58,#6b86c4)"></div>
  <h5>Ilse Marquand</h5><span>Research Assistant Professor</span>
</div>
<div class="person" style="left:620px">
  <div class="portrait" role="img" aria-label="Portrait of Owen Brackley" style="background:linear-gradient(135deg,#d4d4d4,#8e8e8e)"></div>
  <h5>Owen Brackley</h5><span>Neuroscience Principal Investigator</span>
</div>
<div class="person" style="left:900px">
  <div class="portrait" role="img" aria-label="Portrait of Renata Osvik" style="background:linear-gradient(135deg,#6e8a52,#9a6a52)"></div>
  <h5>Renata Osvik</h5><span>Research Assistant Professor</span>
</div>
<div class="people-dots"><span></span><span></span><span></span><span></span><span></span></div>

<section class="pubs">
  <h2>Peer-reviewed publications</h2>
  <p>Lorem Ipsum is simply dummy text of the printing and typesetting industry.</p>
  <a class="btn">Latest Publications</a>
</section>

<footer class="footer">
  <div class="brand"><span class="brand-mark"></span><span class="brand-name">Morvek Lab</span></div>
  <div class="quick">
    <b>Quick Link</b><br>About<br>Research<br>People<br>News / Event<br>Contact
  </div>
  <div class="contact">
    <p class="call">Call. 1-800-555-0147</p>
    <p class="mail">e. info@morveklab.example</p>
    <p class="hours">MON - SAT: 8AM TO 8PM SUN: CLOSE</p>
  </div>
  <div class="social">
    <span style="background:#3b5a9a"></span><span style="background:#2aa3e6"></span><span style="background:#e0302a"></span><span style="background:#1a73b5"></span>
  </div>
  <div class="foot-rule"></div>
  <p class="copyright">© 2019 Morvek Lab All Rights Reserved.</p>
</footer>

</body>
</html>
```